Nonprofit serving disconnected/homeless young adults (age 18-24) needs marketing

There are over 5 Million young adults in the U.S. who are neither working nor in school. Many of them 'aged out' of foster care or group homes, meaning the state doesn't provide care for them when they become an adult at age 18. These young adults have slipped through the cracks of society. Many are homeless, which often times leads to drug use, crime, young pregnancy, violence and prison. QUELVA is a nonprofit dedicated to providing young adults opportunities, resources and experiences to begin building a life they value. We do that via two channels: one our 6-month living program, where participants live expense-free. The requirement is they work full-time, and save at least 75% of their income. At the end of the 6 months, they have the money needed to get into their own place, along with starter furniture and household basics. All potential candidates for housing program come from the resource center QUELVALink. It's where QUELVA offers immediate assistance to young adults, and in-turn we get to know them, and them us. This is essential to see if they're a fit for the housing program. The marketing piece is something young adults (and members of the community) receive. It should 1) be eye catching, maybe something like a path or a road with a phrase "have you chosen the path you're on?" "if given the chance, would you choose something different?" "this is your opportunity to get serious about what matters most to you" "want something different for you life, here's your chance" ...something to that effect. I want the graphics to be big, in your face, something eye catching.

After that, something that says: "here's how"
1. EVERYTHING IN LIFE STARTS WITH THE FIRST STEP: attend orientation on Tuesday if you haven't already
2. YOU WANT TO SOMETHING DIFFERENT FOR YOUR LIFE, YOU NEED TO DO SOMETHING DIFFERENT: our classes are it.
3. YOU WANT TO BE SUCCESSFUL? HANG OUT WITH LIKE-MINDED INDIVIDUALS: attend a volunteer day or fun activity.

(I uploaded our Logo and our new t-shirt design so you can get a look/feel of our current marketing. it should be somewhat modern, "cool" because we're talking to young adults and again - modern design with large graphics.)

Industry/Entity Type

School

```html
<!DOCTYPE html>
<html lang="en">
<head>
<meta charset="utf-8">
<title>QUELVA — Here's Your Chance</title>
<link href="https://fonts.googleapis.com/css2?family=Oswald:wght@500;700&family=Lato:wght@400;700;900&display=swap" rel="stylesheet">
<style>
  :root {
    --teal: #168a74;
    --teal-deep: #0f6e5c;
    --teal-light: #2fb394;
    --ink: #2b2b2b;
    --paper: #ffffff;
  }
  * { margin: 0; padding: 0; box-sizing: border-box; }
  html, body { width: 801px; height: 1200px; overflow: hidden; background: var(--paper); }
  .flyer {
    position: relative; width: 801px; height: 1200px; overflow: hidden;
    background: linear-gradient(180deg, #fff 0%, #fff 60%, #e9e9e9 85%, #dcdcdc 100%);
    font-family: "Lato", sans-serif; color: var(--ink);
  }
  .hero-photo {
    position: absolute; left: 0; top: 0; width: 801px; height: 690px;
    background: linear-gradient(180deg, #f6f6f6 0%, #dedcd9 28%, #b3aea8 45%, #8e8882 62%, #6f6a65 100%);
  }
  .headline {
    position: absolute; left: 0; right: 0; top: 80px; text-align: center;
    font-family: "Oswald", sans-serif; color: var(--ink);
  }
  .headline .kicker { font-size: 33px; font-weight: 500; line-height: 1; }
  .headline .title { font-size: 76px; font-weight: 700; letter-spacing: 1px; line-height: 1.05; margin-top: 8px; }
  .program-band {
    position: absolute; left: 0; top: 456px; width: 801px; height: 234px;
    background: linear-gradient(180deg, rgba(22,138,116,0.92) 0%, rgba(15,110,92,0.96) 100%);
    color: var(--paper); padding: 26px 48px 0 48px;
  }
  .program-band .lead { font-size: 24px; font-weight: 700; line-height: 1.25; }
  .program-band .detail { font-size: 13.6px; line-height: 1.45; margin-top: 6px; }
  .steps { position: absolute; left: 48px; right: 40px; top: 726px; }
  .steps .section-title { font-size: 30px; font-weight: 900; color: var(--teal); letter-spacing: 0.3px; }
  .steps ol { list-style: none; margin-top: 16px; }
  .steps li { font-size: 16px; line-height: 1.35; margin-bottom: 12px; }
  .steps li strong { font-weight: 900; text-transform: uppercase; }
  .brand { position: absolute; left: 48px; top: 1000px; display: flex; align-items: center; gap: 18px; }
  .brand .mark { width: 58px; height: 58px; background: var(--teal); }
  .brand .name { font-family: "Lato", sans-serif; font-weight: 900; font-size: 72px; color: var(--teal); letter-spacing: 4px; line-height: 1; }
  .tagline { position: absolute; left: 48px; top: 1138px; font-size: 12px; letter-spacing: 1.5px; color: var(--teal-deep); }
  .footer-shapes { position: absolute; left: 0; bottom: 0; width: 801px; height: 90px; }
</style>
</head>
<body>
  <main class="flyer">
    <div class="hero-photo" role="img" aria-label="Foggy empty highway stretching into the distance between guardrails"></div>

    <header class="headline">
      <p class="kicker">want something different for you life</p>
      <h1 class="title">HERE'S YOUR CHANCE</h1>
    </header>

    <section class="program-band">
      <p class="lead">We do that via two channels: one our 6-month living program, where participants live expense-free.</p>
      <p class="detail">The requirement is they work full-time, and save at least 75% of their income. At the end of the 6 months, they have the money needed to get into their own place, along with starter furniture and household basics. All potential candidates for housing program come from the resource center QUELVALink. It's where QUELVA offers immediate assistance to young adults, and in-turn we get to know them, and them us. This is essential to see if they're a fit for the housing program.</p>
    </section>

    <section class="steps">
      <h2 class="section-title">HERE'S HOW</h2>
      <ol>
        <li><strong>1. Everything in life starts with the first step</strong><br>attend orientation on Tuesday if you haven't already</li>
        <li><strong>2. You want to something different for your life, you need to do something different:</strong> our classes are it.</li>
        <li><strong>3. You want to be successful? Hang out with like-minded individuals</strong><br>attend a volunteer day or fun activity.</li>
      </ol>
    </section>

    <div class="brand">
      <span class="mark"></span>
      <span class="name">QUELVA</span>
    </div>
    <p class="tagline">Growth. Purpose. Courage. Belonging.</p>

    <svg class="footer-shapes" viewBox="0 0 801 90" aria-hidden="true">
      <polygon points="438,6 801,6 801,90 410,90" fill="var(--teal)"/>
      <rect x="0" y="62" width="801" height="28" fill="var(--teal-light)"/>
    </svg>
  </main>
</body>
</html>
```